Website images and banners needed to be created

We have a website we have not used in a few months that need updated sales banners and images resized for our web devs to upload and update. The site in question is w w w . m a r p e l y . c o m

3 page

```html
<!DOCTYPE html>
<html lang="en">
<head>
<meta charset="utf-8">
<title>Black Friday Sale Banners</title>
<link rel="stylesheet" href="https://fonts.googleapis.com/css2?family=Open+Sans:wght@700;800&display=swap">
<style>
  :root {
    --ink: #000000;
    --paper: #ffffff;
    --sun: #fff200;
    --sun-deep: #ffd400;
    --amber: #ffa000;
    --ember: #ff6a00;
    --muted: #b5b5b5;
    --room-wall: #d9d3cc;
    --room-floor: #a88a70;
    --garden: #6f8d55;
    --shade: #3b3a38;
  }
  html, body {
    margin: 0;
    padding: 0;
    width: 1200px;
    height: 738px;
    overflow: hidden;
    background: var(--paper);
  }
  .banner-sheet {
    display: block;
    width: 1200px;
    height: 738px;
    font-family: "Open Sans", Arial, sans-serif;
  }
  .headline { font-weight: 800; }
  .headline--sun { fill: var(--sun); }
  .headline--ink { fill: var(--ink); }
  .tagline { font-weight: 700; fill: var(--muted); font-size: 13px; letter-spacing: 0.2px; }
  .offer-small { font-weight: 700; fill: var(--paper); }
  .offer-big { font-weight: 800; }
  .offer-big--ink { fill: var(--ink); }
  .offer-big--sun { fill: var(--sun-deep); }
</style>
</head>
<body>
<svg class="banner-sheet" viewBox="0 0 1170 720" width="1200" height="738" preserveAspectRatio="none" xmlns="http://www.w3.org/2000/svg">
  <defs>
    <linearGradient id="roomLeft" x1="0" y1="0" x2="0" y2="1">
      <stop offset="0" stop-color="#9fb38a"/>
      <stop offset="0.45" stop-color="#d8d2ca"/>
      <stop offset="0.7" stop-color="#b59a80"/>
      <stop offset="1" stop-color="#9a7a60"/>
    </linearGradient>
    <linearGradient id="roomRight" x1="0" y1="0" x2="0" y2="1">
      <stop offset="0" stop-color="#e4e2e6"/>
      <stop offset="0.5" stop-color="#cfc7d6"/>
      <stop offset="1" stop-color="#ece9ec"/>
    </linearGradient>
    <linearGradient id="roomDim" x1="0" y1="0" x2="1" y2="0">
      <stop offset="0" stop-color="#4a5a3e"/>
      <stop offset="0.35" stop-color="#6c6a66"/>
      <stop offset="1" stop-color="#8a847d"/>
    </linearGradient>
    <linearGradient id="sunRamp" x1="0" y1="0" x2="1" y2="0">
      <stop offset="0" stop-color="var(--sun)"/>
      <stop offset="0.6" stop-color="var(--sun-deep)"/>
      <stop offset="1" stop-color="var(--amber)"/>
    </linearGradient>
    <linearGradient id="emberRamp" x1="0" y1="0" x2="1" y2="0">
      <stop offset="0" stop-color="var(--sun)"/>
      <stop offset="0.5" stop-color="var(--amber)"/>
      <stop offset="1" stop-color="var(--ember)"/>
    </linearGradient>
  </defs>

  <!-- Top banner -->
  <g class="banner banner--top">
    <rect class="photo photo--bedroom" x="0" y="0" width="700" height="335" fill="url(#roomLeft)" role="img" aria-label="Bedroom with a white metal bed frame, patterned bedding and a rug by large garden windows"/>
    <rect class="photo photo--mattress" x="900" y="0" width="270" height="335" fill="url(#roomRight)" role="img" aria-label="Bedroom with a mattress, purple cushions and a bright window"/>
    <polygon class="panel panel--black" points="350,0 950,0 650,335" fill="var(--ink)"/>
    <polygon class="panel panel--sun" points="650,335 940,22 1170,265 1170,335" fill="url(#sunRamp)"/>

    <text class="headline headline--sun" x="650" y="76" font-size="34" text-anchor="middle">THE BIG</text>
    <text class="headline headline--sun" x="650" y="118" font-size="38" text-anchor="middle">BLACK FRIDAY</text>
    <text class="tagline" x="650" y="163" text-anchor="middle">SALE MUST END SOON</text>

    <text class="offer-small" x="823" y="199" font-size="23">UP TO</text>
    <text class="offer-big offer-big--ink" x="823" y="252" font-size="42">70% OFF</text>
    <text class="offer-small" x="823" y="288" font-size="25">Everything</text>
  </g>

  <!-- Bottom banner -->
  <g class="banner banner--bottom">
    <rect class="photo photo--bedroom-dim" x="0" y="385" width="1170" height="335" fill="url(#roomDim)" role="img" aria-label="Dimmed bedroom with a white metal bed frame and patterned bedding"/>
    <polygon class="sweep" points="0,510 1170,585 1170,720 0,720" fill="url(#emberRamp)"/>
    <polygon class="sweep-gap" points="20,530 1170,592 1170,600" fill="var(--shade)"/>
    <polygon class="sweep-gap" points="10,555 1170,622 1170,634" fill="var(--shade)"/>
    <polygon class="sweep-gap" points="40,572 1170,668 1170,690" fill="var(--shade)"/>

    <text class="offer-small" x="935" y="446" font-size="23">UP TO</text>
    <text class="offer-big offer-big--sun" x="935" y="497" font-size="40">70% OFF</text>
    <text class="offer-small" x="935" y="533" font-size="25">Everything</text>

    <text class="headline headline--ink" x="34" y="643" font-size="32">THE BIG</text>
    <text class="headline headline--ink" x="34" y="686" font-size="38">BLACK FRIDAY</text>
  </g>
</svg>
</body>
</html>
```